CORPORATE AND CLASSY CHRISTMAS CARD (CONTEST)

We want a Christmas card for wealth managers to issue to high net worth clients. Very classy (the target market is clients with investments - typically more than £100,000 which is why the card needs to be very classy). Very corporate. The finished printed card will be a5 to fit existing envelopes. The design will also be used as part of a digital card so i need the image in a format for email as well as print. The brand uses a silver (foil block) on its logo and a specific pan tone ref olive green (reference 620). Not too religious and include a quirky message.

Target Market(s)

High net worth clients - clients with investments, typically more than £100,000 which is why the card needs to be very classy

Requirements
Must have
• The image in a format for email as well as print.
Nice to have
• Very corporate, very classy, the colour scheme of the brand - silver (foil block) and a specific pan ton ref olive green (ref 620) used in a quirky and different way
Should not have
• not too religious

```html
<!DOCTYPE html>
<html lang="en">
<head>
<meta charset="utf-8">
<title>Happy Holidays – Alderley Group</title>
<link rel="stylesheet" href="https://fonts.googleapis.com/css2?family=Pinyon+Script&display=swap">
<style>
  :root {
    --paper: #ffffff;
    --ink-grey: #5b5b5b;
    --ink-dark: #2a2a2a;
    --olive: #8a7a16;
    --olive-soft: #c9bf86;
    --olive-pale: #ece7cf;
    --frame: #222222;
  }
  * { margin: 0; padding: 0; box-sizing: border-box; }
  html, body {
    width: 846px;
    height: 1200px;
    overflow: hidden;
    background: var(--paper);
  }
  .card {
    position: relative;
    width: 846px;
    height: 1200px;
    background: var(--paper);
    border: 1.5px solid var(--frame);
    overflow: hidden;
  }
  .snowflake {
    position: absolute;
    border-radius: 50%;
  }
  .snowflake--solid {
    left: -100px;
    top: 22px;
    width: 230px;
    height: 215px;
    background: radial-gradient(circle at 40% 50%, var(--olive) 0%, var(--olive) 55%, rgba(138,122,22,0.6) 75%, rgba(138,122,22,0) 100%);
  }
  .snowflake--outline {
    left: -110px;
    top: 268px;
    width: 335px;
    height: 262px;
    background: radial-gradient(circle at 35% 50%, var(--olive-soft) 0%, var(--olive-pale) 55%, rgba(236,231,207,0) 100%);
  }
  .snowflake--large {
    left: -370px;
    top: 560px;
    width: 855px;
    height: 720px;
    background: radial-gradient(circle at 57% 46%, var(--olive-soft) 0%, var(--olive-pale) 50%, rgba(236,231,207,0) 78%);
  }
  .greeting {
    position: absolute;
    left: 240px;
    top: 262px;
    font-family: "Pinyon Script", cursive;
    font-weight: 400;
    color: var(--ink-grey);
    font-size: 128px;
    line-height: 148px;
  }
  .greeting__line { display: block; white-space: nowrap; }
  .greeting__line--second { padding-left: 4px; }
  .sender {
    position: absolute;
    left: 612px;
    top: 590px;
    width: 182px;
    text-align: center;
    font-family: "Pinyon Script", cursive;
    font-size: 30px;
    line-height: 36px;
    color: var(--ink-dark);
  }
</style>
</head>
<body>
  <main class="card">
    <div class="snowflake snowflake--solid" role="img" aria-label="Solid olive snowflake ornament"></div>
    <div class="snowflake snowflake--outline" role="img" aria-label="Outlined snowflake ornament with olive flower motifs"></div>
    <div class="snowflake snowflake--large" role="img" aria-label="Large outlined olive snowflake ornament with floral motifs"></div>

    <h1 class="greeting">
      <span class="greeting__line">Happy</span>
      <span class="greeting__line greeting__line--second">Holidays!</span>
    </h1>

    <p class="sender">Alderley Group</p>
  </main>
</body>
</html>
```